R T Security Flyer - Security Based Company

Security company offering installation of CCTV and Intruder alarm systems mainly but not limited to home alarms. Feel free to be creative

Target Market(s)

Residential and Commercial properties, Facility Managers, local business

Requirements
Must have
• smart professional finish, logo and latest up to date pictures if on kit

```html
<!DOCTYPE html>
<html lang="en">
<head>
<meta charset="utf-8">
<title>R T Security Systems – Flyer</title>
<link href="https://fonts.googleapis.com/css2?family=Open+Sans:wght@400;600;700;800&display=swap" rel="stylesheet">
<style>
  :root{
    --backdrop:#c8c8c8;
    --paper:#ffffff;
    --brand:#ea5127;
    --brand-warm:#f08a3c;
    --ink:#222222;
    --muted:#5a5a5a;
    --panel:#ececec;
    --night:#0b0b0b;
    --rule:#e0663f;
  }
  *{box-sizing:border-box;margin:0;padding:0}
  html,body{width:1200px;height:1200px;overflow:hidden}
  body{background:var(--backdrop);font-family:"Open Sans",Arial,sans-serif;color:var(--ink);position:relative}
  .page{position:absolute;top:258px;width:528px;height:683px;background:var(--paper);overflow:hidden}
  .page--front{left:62px}
  .page--back{left:610px}

  /* front header */
  .masthead{position:absolute;left:0;top:0;width:100%;height:99px}
  .wordmark{position:absolute;left:24px;top:36px;display:flex;align-items:center;gap:9px}
  .wordmark__dot{width:26px;height:26px;border-radius:50%;background:var(--brand);flex:none}
  .wordmark__name{color:var(--ink);font-weight:700;font-size:19px;line-height:26px;white-space:nowrap}
  .masthead__divider{position:absolute;left:293px;top:33px;width:2px;height:34px;background:var(--rule)}
  .masthead__web{position:absolute;right:18px;top:41px;font-size:12px;color:var(--muted)}
  .masthead__web b{color:var(--brand);font-weight:700}

  .hero{position:absolute;left:0;top:99px;width:528px;height:188px;background:linear-gradient(100deg,#b9bcc0 0%,#8e9194 45%,#6e6b66 70%,#9a968f 100%)}
  .hero__title{position:absolute;left:82px;top:105px;color:#fff;font-weight:800;font-size:25px;line-height:31px;letter-spacing:.3px}

  .checklist{list-style:none}
  .checklist li{position:relative;padding-left:22px}
  .checklist svg{position:absolute;left:0;top:1px;width:14px;height:14px}
  .checklist--front{position:absolute;left:80px;top:314px;width:390px;font-size:10.5px;line-height:12.5px}
  .checklist--front li{margin-bottom:8.5px}

  .callout{position:absolute;left:0;top:525px;width:528px;height:95px;background:linear-gradient(90deg,var(--brand) 0%,var(--brand-warm) 100%)}
  .callout svg{position:absolute;left:80px;top:29px;width:40px;height:40px}
  .callout__text{position:absolute;left:134px;top:28px;width:345px;color:#fff;font-weight:700;font-size:11.5px;line-height:14.5px}

  .contact-bar{position:absolute;left:0;top:620px;width:528px;height:63px;background:var(--panel)}
  .badge-listing{position:absolute;left:18px;top:20px;width:156px;height:24px;border-radius:4px;background:#d5d9e6}
  .badge-seal{position:absolute;left:194px;top:13px;width:37px;height:37px;border-radius:50%;border:3px solid #2f4e93;background:#fff}
  .badge-seal-tag{position:absolute;left:236px;top:24px;width:30px;height:14px;border-radius:2px;background:#c9d1e4}
  .contact-bar__divider{position:absolute;left:293px;top:14px;width:2px;height:34px;background:var(--rule)}
  .contact-bar__phone{position:absolute;left:314px;top:13px;font-size:16px;font-weight:700;display:flex;align-items:center;gap:5px}
  .contact-bar__mail{position:absolute;left:314px;top:35px;font-size:10.5px;display:flex;align-items:center;gap:5px}

  /* back page */
  .intro{position:absolute;left:126px;top:23px;width:360px;font-size:10.5px;line-height:12.5px}
  .intro p{margin-bottom:13px}
  .checklist--back{position:absolute;left:126px;top:87px;width:370px;font-size:10.5px;line-height:12.5px}
  .checklist--back li{margin-bottom:8.5px}

  .photo{position:absolute;top:287px;height:151px}
  .photo--phone{left:0;width:256px;background:linear-gradient(110deg,#e8e4df 0%,#b28a63 45%,#7a5638 100%)}
  .photo--panel{left:260px;width:268px;background:linear-gradient(90deg,#e6e7e8 0%,#cfd4d8 40%,#b7b8b4 70%,#e4e2dc 100%)}

  .services{position:absolute;left:25px;top:471px;width:90px}
  .services h3{font-size:9.5px;font-weight:700;margin-bottom:5px}
  .services ul{list-style:none;font-size:8.5px;line-height:10.5px;color:var(--muted)}
  .services li{position:relative;padding-left:8px;margin-bottom:3.5px}
  .services li::before{content:"";position:absolute;left:0;top:4px;width:3px;height:3px;border-radius:50%;background:var(--brand)}
  .story{position:absolute;left:126px;top:472px;width:380px;font-size:10.5px;line-height:12.5px}
  .story p{margin-bottom:8px}

  .closing-bar{position:absolute;left:0;top:620px;width:528px;height:63px;background:var(--night);border-top:2px solid var(--brand)}
  .closing-bar__name{position:absolute;left:25px;top:13px;color:#fff;font-size:10.5px;font-weight:700}
  .closing-bar__addr{position:absolute;left:25px;top:33px;color:#fff;font-size:10.5px;display:flex;align-items:center;gap:6px}
  .closing-bar .wordmark{left:auto;right:25px;top:19px;gap:7px}
  .closing-bar .wordmark__dot{width:20px;height:20px}
  .closing-bar .wordmark__name{color:#fff;font-size:14px;line-height:20px}
</style>
</head>
<body>

<section class="page page--front">
  <header class="masthead">
    <div class="wordmark">
      <div class="wordmark__dot"></div>
      <div class="wordmark__name">R T Security Systems</div>
    </div>
    <div class="masthead__divider"></div>
    <div class="masthead__web">www.<b>rtsecuritysystems</b>.co.uk</div>
  </header>

  <div class="hero" role="img" aria-label="Photo of a finger pressing an alarm keypad reading Welcome Home in a hallway">
    <h1 class="hero__title">ARE YOU LOOKING TO KEEP<br>YOU OR YOUR PREMISES SAFE?</h1>
  </div>

  <ul class="checklist checklist--front">
    <li><svg viewBox="0 0 14 14"><rect x="1" y="3" width="10" height="10" fill="none" stroke="#222" stroke-width="1.5"/><path d="M3.5 7.5l2.5 2.5L13 1.5" fill="none" stroke="#ea5127" stroke-width="2"/></svg>We install, maintain and repair all intruder alarms, CCTV, intercom and access control.</li>
    <li><svg viewBox="0 0 14 14"><rect x="1" y="3" width="10" height="10" fill="none" stroke="#222" stroke-width="1.5"/><path d="M3.5 7.5l2.5 2.5L13 1.5" fill="none" stroke="#ea5127" stroke-width="2"/></svg>View, control and manage your security systems anywhere in the world with smartphone apps.</li>
    <li><svg viewBox="0 0 14 14"><rect x="1" y="3" width="10" height="10" fill="none" stroke="#222" stroke-width="1.5"/><path d="M3.5 7.5l2.5 2.5L13 1.5" fill="none" stroke="#ea5127" stroke-width="2"/></svg>Feel at ease with monitoring services and police response tailored to suit you and your business.</li>
    <li><svg viewBox="0 0 14 14"><rect x="1" y="3" width="10" height="10" fill="none" stroke="#222" stroke-width="1.5"/><path d="M3.5 7.5l2.5 2.5L13 1.5" fill="none" stroke="#ea5127" stroke-width="2"/></svg>We can takeover any existing security system and offer maintenance checks to guarantee the best performance for you and your premises.</li>
    <li><svg viewBox="0 0 14 14"><rect x="1" y="3" width="10" height="10" fill="none" stroke="#222" stroke-width="1.5"/><path d="M3.5 7.5l2.5 2.5L13 1.5" fill="none" stroke="#ea5127" stroke-width="2"/></svg>We understand that being security conscious is ever increasing, protecting your property and family is a number one priority.</li>
    <li><svg viewBox="0 0 14 14"><rect x="1" y="3" width="10" height="10" fill="none" stroke="#222" stroke-width="1.5"/><path d="M3.5 7.5l2.5 2.5L13 1.5" fill="none" stroke="#ea5127" stroke-width="2"/></svg>Our fully insured and accredited team offer quality, safety and cost efficiency throughout and whole process.</li>
  </ul>

  <div class="callout">
    <svg viewBox="0 0 40 40" fill="none" stroke="#fff" stroke-width="2" stroke-linejoin="round" stroke-linecap="round"><path d="M8 6l6 0 3 8-4 3c2 5 5 8 10 10l3-4 8 3v6c0 2-2 3-4 3C17 35 5 23 5 9c0-2 1-3 3-3z"/><path d="M24 5a11 11 0 0 1 11 11"/><path d="M24 10a6 6 0 0 1 6 6"/></svg>
    <p class="callout__text">If you are looking to improve the security in your home, office or commercial property then call a member of our team today for a free quote.</p>
  </div>

  <footer class="contact-bar">
    <div class="badge-listing"></div>
    <div class="badge-seal"></div>
    <div class="badge-seal-tag"></div>
    <div class="contact-bar__divider"></div>
    <div class="contact-bar__phone"><svg width="12" height="12" viewBox="0 0 12 12"><path d="M2 1h2.5l1 3-1.5 1c.7 1.5 1.6 2.4 3 3l1-1.5 3 1V10c0 .6-.5 1-1 1C5 11 1 7 1 2c0-.5.4-1 1-1z" fill="#777"/></svg>01632 960 418</div>
    <div class="contact-bar__mail"><svg width="12" height="9" viewBox="0 0 12 9"><rect width="12" height="9" rx="1" fill="#777"/><path d="M1 1l5 4 5-4" fill="none" stroke="#fff" stroke-width="1"/></svg>operations@rtsecuritysystems.co.uk</div>
  </footer>
</section>

<section class="page page--back">
  <div class="intro">
    <p>R T Security Systems are using the latest cloud-based technology to stay connected with your home and business 24/7.</p>
    <p>Some benefits of cloud services are:</p>
  </div>

  <ul class="checklist checklist--back">
    <li><svg viewBox="0 0 14 14"><rect x="1" y="3" width="10" height="10" fill="none" stroke="#222" stroke-width="1.5"/><path d="M3.5 7.5l2.5 2.5L13 1.5" fill="none" stroke="#ea5127" stroke-width="2"/></svg>High level support 24/7</li>
    <li><svg viewBox="0 0 14 14"><rect x="1" y="3" width="10" height="10" fill="none" stroke="#222" stroke-width="1.5"/><path d="M3.5 7.5l2.5 2.5L13 1.5" fill="none" stroke="#ea5127" stroke-width="2"/></svg>Reduce engineer call outs and running costs</li>
    <li><svg viewBox="0 0 14 14"><rect x="1" y="3" width="10" height="10" fill="none" stroke="#222" stroke-width="1.5"/><path d="M3.5 7.5l2.5 2.5L13 1.5" fill="none" stroke="#ea5127" stroke-width="2"/></svg>Identify issues in advance</li>
    <li><svg viewBox="0 0 14 14"><rect x="1" y="3" width="10" height="10" fill="none" stroke="#222" stroke-width="1.5"/><path d="M3.5 7.5l2.5 2.5L13 1.5" fill="none" stroke="#ea5127" stroke-width="2"/></svg>Remotely manage systems to ensure correct operation</li>
    <li><svg viewBox="0 0 14 14"><rect x="1" y="3" width="10" height="10" fill="none" stroke="#222" stroke-width="1.5"/><path d="M3.5 7.5l2.5 2.5L13 1.5" fill="none" stroke="#ea5127" stroke-width="2"/></svg>Remote health checks carried out to keep your system performing as it should</li>
    <li><svg viewBox="0 0 14 14"><rect x="1" y="3" width="10" height="10" fill="none" stroke="#222" stroke-width="1.5"/><path d="M3.5 7.5l2.5 2.5L13 1.5" fill="none" stroke="#ea5127" stroke-width="2"/></svg>Automatically update your system with the latest releases via cloud application software</li>
    <li><svg viewBox="0 0 14 14"><rect x="1" y="3" width="10" height="10" fill="none" stroke="#222" stroke-width="1.5"/><path d="M3.5 7.5l2.5 2.5L13 1.5" fill="none" stroke="#ea5127" stroke-width="2"/></svg>Interact, control and integrate your security system like never before</li>
  </ul>

  <div class="photo photo--phone" role="img" aria-label="Photo of hands holding a smartphone showing a security app beside a coffee cup on a wooden table"></div>
  <div class="photo photo--panel" role="img" aria-label="Photo of a wall-mounted touchscreen alarm panel in a modern kitchen"></div>

  <div class="services">
    <h3>Our Services</h3>
    <ul>
      <li>Intruder Alarm Systems</li>
      <li>CCTV</li>
      <li>Access Control</li>
      <li>Door Entry</li>
      <li>Fire Alarm</li>
      <li>Detection / Security Lighting</li>
    </ul>
  </div>

  <div class="story">
    <p>With the new cloud-based system we can check the alarm performance anytime you need it. This gives us the capability to assist you in any of your needs, be that changing user codes or system configuration. We are always there, working in the background to make sure you have the support and help you need. This is taking alarm systems into the future and leaving the stand-alone systems in the past.</p>
    <p>R T Security Systems are always there, always available, wherever and whenever you need us.</p>
  </div>

  <footer class="closing-bar">
    <div class="closing-bar__name">R T Security Systems</div>
    <div class="closing-bar__addr"><svg width="10" height="13" viewBox="0 0 10 13"><path d="M5 0a5 5 0 0 1 5 5c0 3.5-5 8-5 8S0 8.5 0 5a5 5 0 0 1 5-5z" fill="#ea5127"/><circle cx="5" cy="5" r="1.8" fill="#0b0b0b"/></svg>14 Harlow Lane, Brentwood, Essex, CM15 2QX</div>
    <div class="wordmark">
      <div class="wordmark__dot"></div>
      <div class="wordmark__name">R T Security Systems</div>
    </div>
  </footer>
</section>

</body>
</html>
```